New Logo, New Business Cards! Looking for Refresh

We're in the process of modernizing our entire organization, and with that came the redesign of our logo (attached). We're looking for a designer to develop our new business cards.
Looking for a design that will bring the company in 2020 and help showcase our new logo. Work with the colors of the logo. Feel free to experiment with the logo in white or black if you want. Both now attached.
Industry/Entity Type
Non Profit
Contact Information for Business Card
Address:
48315 Pelham Crescent, Suite 512
Ashbury Glen, MB, K7R 2M5
Name: Dorian Welbeck, MBA
Position: Executive Director
Telephone: 905-371-6248, Ext. 817
Cell Phone: 416-573-2064
Email: dorian@qorvenu.ca
Website: www.qorvenu.ca
Look and feel
Each slider illustrates characteristics of the customer's brand and the style your logo design should communicate.

```html
<!DOCTYPE html>
<html lang="en">
<head>
<meta charset="utf-8">
<title>Qorvenu Business Card</title>
<link rel="stylesheet" href="https://fonts.googleapis.com/css2?family=Poppins:wght@400;600;800&display=swap">
<style>
  :root {
    --green-dark: #0b3d21;
    --green: #3f9a2e;
    --ink: #123a22;
    --paper: #ffffff;
    --backdrop: #e9e6df;
    --deco-grey: #dfe3de;
    --deco-green: #e6f0e1;
  }
  * { margin: 0; padding: 0; box-sizing: border-box; }
  html, body { width: 1189px; height: 1200px; overflow: hidden; }
  body {
    background: var(--backdrop);
    font-family: "Poppins", sans-serif;
    position: relative;
  }
  .card {
    position: absolute;
    left: 169px;
    width: 851px;
    height: 487px;
    border-radius: 30px;
    overflow: hidden;
    box-shadow: 0 10px 24px rgba(0,0,0,0.25);
  }
  /* Front */
  .card-front { top: 110px; background: var(--green-dark); color: var(--paper); }
  .front-brand {
    position: absolute; left: 0; right: 0; top: 196px;
    display: flex; justify-content: center; align-items: center; gap: 18px;
  }
  .brand-square { width: 54px; height: 54px; background: currentColor; display: block; flex: none; }
  .front-brand .brand-name { font-size: 74px; font-weight: 800; line-height: 1; letter-spacing: 1px; }
  .front-url {
    position: absolute; left: 0; right: 0; top: 358px;
    text-align: center; font-size: 20px; font-weight: 400; letter-spacing: 4px;
  }
  /* Back */
  .card-back { top: 641px; background: var(--paper); color: var(--ink); }
  .back-deco {
    position: absolute; left: 490px; top: 0; width: 361px; height: 339px;
    background: linear-gradient(90deg, var(--deco-grey) 0%, var(--deco-green) 55%, #f6eaea 100%);
    opacity: 0.85;
  }
  .back-brand {
    position: absolute; left: 52px; top: 96px;
    display: flex; align-items: center; gap: 14px; color: var(--green-dark);
  }
  .back-brand .brand-square { width: 46px; height: 46px; background: var(--green); }
  .back-brand .brand-name { font-size: 62px; font-weight: 800; line-height: 1; letter-spacing: 1px; }
  .back-url {
    position: absolute; right: 51px; top: 70px;
    font-size: 18px; font-weight: 400; color: var(--ink);
  }
  .person { position: absolute; left: 52px; top: 256px; }
  .person-name { font-size: 28px; font-weight: 600; line-height: 1.2; color: var(--ink); }
  .person-role { font-size: 20px; font-weight: 400; color: var(--green); line-height: 1.2; }
  .divider { position: absolute; left: 52px; top: 340px; width: 748px; height: 2px; background: var(--green); }
  .contacts { position: absolute; left: 52px; top: 362px; list-style: none; }
  .contacts li { display: flex; align-items: center; gap: 8px; font-size: 20px; line-height: 29px; }
  .contacts svg { width: 22px; height: 22px; flex: none; }
  .address { position: absolute; left: 520px; top: 366px; font-size: 20px; line-height: 29px; font-style: normal; }
  .band { position: absolute; bottom: 0; height: 18px; width: 50%; }
  .band-dark { left: 0; background: var(--green-dark); }
  .band-light { right: 0; background: var(--green); }
</style>
</head>
<body>
  <section class="card card-front">
    <div class="front-brand">
      <span class="brand-square"></span>
      <span class="brand-name">QORVENU</span>
    </div>
    <p class="front-url">www.qorvenu.ca</p>
  </section>

  <section class="card card-back">
    <div class="back-deco" role="img" aria-label="Faint enlarged emblem: open book with gavel and leaf"></div>
    <div class="back-brand">
      <span class="brand-square"></span>
      <span class="brand-name">QORVENU</span>
    </div>
    <p class="back-url">www.qorvenu.ca</p>

    <div class="person">
      <p class="person-name">Dorian Welbeck, MBA</p>
      <p class="person-role">Executive Director</p>
    </div>
    <div class="divider"></div>

    <ul class="contacts">
      <li>
        <svg viewBox="0 0 22 22"><circle cx="11" cy="11" r="10.5" fill="#3f9a2e"/><path d="M7.5 5.5l2 2.5-1.2 1.4c.8 1.7 2 2.9 3.6 3.7l1.4-1.2 2.5 2-1.3 2c-4-.6-7.3-3.9-8-8z" fill="#fff"/></svg>
        204-371-6248, Ext. 817
      </li>
      <li>
        <svg viewBox="0 0 22 22"><circle cx="11" cy="11" r="10.5" fill="#3f9a2e"/><rect x="7.5" y="5" width="7" height="12" rx="1.2" fill="#fff"/><rect x="8.8" y="6.8" width="4.4" height="7.5" fill="#3f9a2e"/></svg>
        431-573-2064
      </li>
      <li>
        <svg viewBox="0 0 22 22"><circle cx="11" cy="11" r="10.5" fill="#3f9a2e"/><rect x="5.5" y="7" width="11" height="8" fill="#fff"/><path d="M5.5 7l5.5 4.5L16.5 7" fill="none" stroke="#3f9a2e" stroke-width="1.2"/></svg>
        dorian@qorvenu.ca
      </li>
    </ul>

    <address class="address">
      48315 Pelham Crescent<br>
      Suite 512<br>
      Ashbury Glen, MB, K7R 2M5
    </address>

    <div class="band band-dark"></div>
    <div class="band band-light"></div>
  </section>
</body>
</html>
```